Label for LiPo Battery Product for RC Hobby Industry

We need your creativity for a new lithium battery label design. We aim to make our product visually appealing and distinct from competitors. Your design skills are crucial for this task, and we're excited to work with you.
Our main label feature is the colour tag profile, designed to easily identify battery category and power level with a 2-way colour band. Inspired by a tool company that uses a consistent colour profile to identify Phillips head sizing across their range.
The design should be modern, clear, convey speed and suitable for both professional and consumer markets.
Target Market(s)
RC, Drone, Camera community. 20-30 year old.
Industry/Entity Type
Battery, Drone Industry, RC Car
Requirements
Must have
- 2-Way colour tag identity profiling, clear text at 100% scale
Nice to have
- Text and graphic alignment. Comfortable padding and formatting. Colour tag profile, clear text."
Should not have
- Basic, stock looking image.

```html
<!DOCTYPE html>
<html lang="en">
<head>
<meta charset="utf-8">
<title>PX620 LiPo Battery Label</title>
<link href="https://fonts.googleapis.com/css2?family=Barlow+Condensed:ital,wght@0,500;0,700;1,700&family=Oswald:wght@500;700&family=Russo+One&display=swap" rel="stylesheet">
<style>
  :root {
    --page-bg: #dfe2e5;
    --label-red: #b3182f;
    --label-red-deep: #8e0f22;
    --label-teal: #1f9aa5;
    --label-teal-deep: #137983;
    --label-black: #06090c;
    --circuit-glow: #0e3140;
    --label-white: #ffffff;
    --band-silver: #d3d5d7;
    --ink: #111111;
  }
  html, body {
    margin: 0;
    padding: 0;
    width: 1002px;
    height: 1200px;
    overflow: hidden;
    background: var(--page-bg);
  }
  .canvas {
    position: relative;
    width: 1002px;
    height: 1200px;
  }
  .battery-label {
    position: absolute;
    left: 41px;
    top: 352px;
    width: 920px;
    height: 496px;
    display: block;
  }
  .brand-name { font-family: "Russo One", sans-serif; fill: var(--ink); }
  .model-code {
    font-family: "Oswald", sans-serif;
    font-weight: 700;
    fill: var(--label-white);
  }
  .spec-tag-text {
    font-family: "Barlow Condensed", sans-serif;
    font-weight: 700;
    font-style: italic;
    fill: var(--label-white);
  }
  .energy-text { font-family: "Oswald", sans-serif; font-weight: 700; fill: var(--label-white); }
  .capacity-text { font-family: "Oswald", sans-serif; font-weight: 500; fill: var(--label-white); }
  .tagline { font-family: "Oswald", sans-serif; font-weight: 500; fill: var(--ink); }
</style>
</head>
<body>
<main class="canvas">
  <svg class="battery-label" viewBox="0 0 1280 690" xmlns="http://www.w3.org/2000/svg">
    <defs>
      <radialGradient id="circuit-field" cx="0.55" cy="0.4" r="0.7">
        <stop offset="0" stop-color="var(--circuit-glow)"/>
        <stop offset="1" stop-color="var(--label-black)"/>
      </radialGradient>
      <linearGradient id="red-panel" x1="0" x2="1" y1="0" y2="0">
        <stop offset="0" stop-color="var(--label-red-deep)"/>
        <stop offset="0.5" stop-color="var(--label-red)"/>
        <stop offset="1" stop-color="var(--label-red)"/>
      </linearGradient>
      <linearGradient id="silver-band" x1="0" x2="1" y1="0" y2="0">
        <stop offset="0" stop-color="var(--label-white)"/>
        <stop offset="0.5" stop-color="var(--band-silver)"/>
        <stop offset="1" stop-color="var(--label-white)"/>
      </linearGradient>
      <linearGradient id="brand-tab" x1="0" x2="1" y1="0" y2="0">
        <stop offset="0" stop-color="#e4e5e6"/>
        <stop offset="0.5" stop-color="var(--label-white)"/>
        <stop offset="1" stop-color="#cfd1d3"/>
      </linearGradient>
      <linearGradient id="teal-tag" x1="0" x2="1" y1="0" y2="0">
        <stop offset="0" stop-color="var(--label-teal)"/>
        <stop offset="1" stop-color="var(--label-teal-deep)"/>
      </linearGradient>
    </defs>

    <rect class="circuit-backdrop" x="0" y="0" width="1280" height="690" fill="url(#circuit-field)" role="img" aria-label="Glowing blue circuit board traces on black"/>

    <path class="side-panel" d="M0 0 H280 Q310 0 310 30 V690 H0 Z" fill="url(#red-panel)"/>
    <rect class="bottom-band" x="0" y="648" width="1280" height="42" fill="url(#red-panel)"/>

    <path class="tagline-band" d="M325 540 H1280 V648 H405 Q340 648 332 590 Z" fill="url(#silver-band)"/>

    <g class="spec-tags">
      <g class="spec-tag">
        <rect x="35" y="215" width="275" height="14" fill="var(--label-red-deep)"/>
        <rect x="45" y="100" width="295" height="115" fill="url(#teal-tag)"/>
        <text class="spec-tag-text" x="80" y="188" font-size="84">120C</text>
      </g>
      <line x1="55" y1="258" x2="290" y2="258" stroke="var(--label-red-deep)" stroke-width="3"/>
      <g class="spec-tag">
        <rect x="35" y="398" width="275" height="14" fill="var(--label-red-deep)"/>
        <rect x="45" y="283" width="295" height="115" fill="url(#teal-tag)"/>
        <text class="spec-tag-text" x="78" y="371" font-size="84">6 CELLS</text>
      </g>
      <line x1="55" y1="440" x2="290" y2="440" stroke="var(--label-red-deep)" stroke-width="3"/>
      <g class="spec-tag">
        <rect x="35" y="582" width="275" height="14" fill="var(--label-red-deep)"/>
        <rect x="45" y="465" width="295" height="117" fill="url(#teal-tag)"/>
        <text class="spec-tag-text" x="78" y="554" font-size="84">22.2V</text>
      </g>
    </g>

    <path class="brand-tab" d="M555 0 H1115 L1075 118 Q1066 145 1038 145 H632 Q604 145 595 118 Z" fill="url(#brand-tab)"/>
    <text class="brand-name" x="835" y="110" font-size="78" text-anchor="middle" textLength="360" lengthAdjust="spacingAndGlyphs">KARVEN</text>

    <text class="model-code" x="840" y="322" font-size="170" text-anchor="middle" textLength="640" lengthAdjust="spacingAndGlyphs">PX620</text>

    <polygon class="energy-band" points="440,352 892,352 852,428 900,500 445,500 395,428" fill="var(--label-red)"/>
    <polygon class="capacity-band" points="935,352 1280,352 1280,500 920,500 875,428" fill="var(--label-teal)"/>
    <text class="energy-text" x="458" y="472" font-size="118" textLength="362" lengthAdjust="spacingAndGlyphs">1300WH</text>
    <text class="capacity-text" x="965" y="472" font-size="118" textLength="240" lengthAdjust="spacingAndGlyphs">1.3Ah</text>

    <text class="tagline" x="452" y="613" font-size="38" textLength="758" lengthAdjust="spacingAndGlyphs">PERFORMANCE | ARMOUR PROTECTION | ADVANCED INSULATION</text>
  </svg>
</main>
</body>
</html>
```